Design für 3-Monatskalender
Zielgruppe
Hallo, wir benötigen ein Design bzw. fertige Druckdaten für einen 3 Monatskalender mit den Feiertagen aus DE, AT und CH.
Format ist DIN A6, der Kalender wird benötigt für das Jahr 2024 und 2025.
Aufgabenstellung
Format: DIN A6
Kalendarium 2024 und 2025
Feiertage aus DE, AT und CH
Beispiel anbei, wichtig ist, das wir einen Magnetischen Ring als Datumsschieber nehmen. Der Ring hat die Maße: Durchmesser = 12mm Innendruchmesser = 10mm

```html
<!DOCTYPE html>
<html lang="de">
<head>
<meta charset="utf-8">
<title>3-Monatskalender Dezember 2024 – Februar 2025</title>
<link rel="stylesheet" href="https://fonts.googleapis.com/css2?family=Playfair+Display:wght@800&family=Cormorant+Garamond:wght@600;700&family=Fira+Sans:wght@300&display=swap">
<style>
:root{
  --paper:#f7f2ef;
  --band:#d3b89c;
  --band-line:#e2d2c1;
  --gold:#d1a065;
  --ink:#1e1a17;
  --week:#5f5952;
  --sunday:#ffffff;
  --ring:#c0141f;
  --cols:74px 100px 85px 85px 97px 99px 86px 85px 92px 69px;
}
*{margin:0;padding:0;box-sizing:border-box}
html,body{width:872px;height:1200px;overflow:hidden;background:var(--paper)}
.calendar{position:relative;width:872px;height:1200px;background:var(--paper)}
.month{position:absolute;left:0;width:872px}
.month-title{position:absolute;left:68px;font:800 28px/32px "Playfair Display",serif;color:var(--gold);white-space:nowrap;letter-spacing:-.3px}
.month-rule{position:absolute;right:148px;height:2px;background:linear-gradient(90deg,rgba(209,160,101,.35),var(--gold) 25%,var(--gold) 75%,rgba(209,160,101,.35));border-radius:1px}
.month-year{position:absolute;right:69px;font:800 27px/32px "Playfair Display",serif;color:var(--gold)}
.weekday-row{position:absolute;left:0;right:0;display:grid;grid-template-columns:var(--cols);font:300 12.3px/12.6px "Fira Sans",sans-serif;color:var(--ink)}
.weekday-row span{text-align:right;white-space:nowrap}
.weekday-row .week-label{grid-column:2;text-align:left;color:var(--gold)}
.weeks{position:absolute;left:0;width:872px;background:var(--band)}
.week{display:grid;grid-template-columns:var(--cols);align-items:center;height:43.4px;border-top:1px solid var(--band-line);font:600 30px/1 "Cormorant Garamond",serif;color:var(--ink)}
.week:first-child{border-top:none}
.week span{text-align:right}
.week .kw{grid-column:2;text-align:left;color:var(--week);font-weight:700;font-size:29px}
.week .sun{color:var(--sunday)}
.holidays{position:absolute;left:0;top:1043px;width:872px;height:157px;font:300 11.6px/14.2px "Fira Sans",sans-serif;color:var(--ink)}
.holidays .label{position:absolute;left:74px;top:18px;color:var(--gold);line-height:17.6px}
.holiday-list{position:absolute;left:0;top:18px;display:grid}
.holiday-list dt{text-align:right;padding-right:4px;border-right:1px solid var(--band);white-space:nowrap}
.holiday-list dd{padding-left:5px;color:var(--gold);white-space:nowrap}
.list-de{grid-template-columns:324px auto}
.list-en{grid-template-columns:548px auto}
.list-fr{grid-template-columns:749px auto}
.date-ring{position:absolute;left:478px;top:190px;width:100px;height:100px;overflow:visible}
</style>
</head>
<body>
<main class="calendar">

  <!-- Dezember 2024 -->
  <section class="month" style="top:0">
    <h2 class="month-title" style="top:38px">Dezember . December . Décembre</h2>
    <div class="month-rule" style="left:497px;top:53px"></div>
    <div class="month-year" style="top:39px">2024</div>
    <div class="weekday-row" style="top:81px">
      <span class="week-label">Woche<br>Week<br>Semaine</span>
      <span>Montag<br>Monday<br>Lundi</span><span>Dienstag<br>Tuesday<br>Mardi</span><span>Mittwoch<br>Wednesday<br>Mercredi</span><span>Donnerstag<br>Thursday<br>Jeudi</span><span>Freitag<br>Friday<br>Vendredi</span><span>Samstag<br>Saturday<br>Samedi</span><span>Sonntag<br>Sunday<br>Dimanche</span>
    </div>
  </section>
  <div class="weeks" style="top:132px">
    <div class="week"><span class="kw">48</span><span></span><span></span><span></span><span></span><span></span><span></span><span class="sun">1</span></div>
    <div class="week"><span class="kw">49</span><span>2</span><span>3</span><span>4</span><span>5</span><span>6</span><span>7</span><span class="sun">8</span></div>
    <div class="week"><span class="kw">50</span><span>9</span><span>10</span><span>11</span><span>12</span><span>13</span><span>14</span><span class="sun">15</span></div>
    <div class="week"><span class="kw">51</span><span>16</span><span>17</span><span>18</span><span>19</span><span>20</span><span>21</span><span class="sun">22</span></div>
    <div class="week"><span class="kw">52</span><span>23</span><span>24</span><span>25</span><span>26</span><span>27</span><span>28</span><span class="sun">29</span></div>
    <div class="week"><span class="kw">53</span><span>30</span><span>31</span><span></span><span></span><span></span><span></span><span></span></div>
  </div>

  <!-- Januar 2025 -->
  <section class="month" style="top:0">
    <h2 class="month-title" style="top:409px">Januar . January . Janvier</h2>
    <div class="month-rule" style="left:389px;top:426px"></div>
    <div class="month-year" style="top:411px">2025</div>
    <div class="weekday-row" style="top:448px">
      <span class="week-label">Woche<br>Week<br>Semaine</span>
      <span>Montag<br>Monday<br>Lundi</span><span>Dienstag<br>Tuesday<br>Mardi</span><span>Mittwoch<br>Wednesday<br>Mercredi</span><span>Donnerstag<br>Thursday<br>Jeudi</span><span>Freitag<br>Friday<br>Vendredi</span><span>Samstag<br>Saturday<br>Samedi</span><span>Sonntag<br>Sunday<br>Dimanche</span>
    </div>
  </section>
  <div class="weeks" style="top:502px">
    <div class="week"><span class="kw">1</span><span></span><span></span><span>1</span><span>2</span><span>3</span><span>4</span><span class="sun">5</span></div>
    <div class="week"><span class="kw">2</span><span>6</span><span>7</span><span>8</span><span>9</span><span>10</span><span>11</span><span class="sun">12</span></div>
    <div class="week"><span class="kw">3</span><span>13</span><span>14</span><span>15</span><span>16</span><span>17</span><span>18</span><span class="sun">19</span></div>
    <div class="week"><span class="kw">4</span><span>20</span><span>21</span><span>22</span><span>23</span><span>24</span><span>25</span><span class="sun">26</span></div>
    <div class="week"><span class="kw">5</span><span>27</span><span>28</span><span>29</span><span>30</span><span>31</span><span></span><span></span></div>
  </div>

  <!-- Februar 2025 -->
  <section class="month" style="top:0">
    <h2 class="month-title" style="top:735px">Februar . February . Février</h2>
    <div class="month-rule" style="left:428px;top:753px"></div>
    <div class="month-year" style="top:737px">2025</div>
    <div class="weekday-row" style="top:774px">
      <span class="week-label">Woche<br>Week<br>Semaine</span>
      <span>Montag<br>Monday<br>Lundi</span><span>Dienstag<br>Tuesday<br>Mardi</span><span>Mittwoch<br>Wednesday<br>Mercredi</span><span>Donnerstag<br>Thursday<br>Jeudi</span><span>Freitag<br>Friday<br>Vendredi</span><span>Samstag<br>Saturday<br>Samedi</span><span>Sonntag<br>Sunday<br>Dimanche</span>
    </div>
  </section>
  <div class="weeks" style="top:825px">
    <div class="week"><span class="kw">5</span><span></span><span></span><span></span><span></span><span></span><span>1</span><span class="sun">2</span></div>
    <div class="week"><span class="kw">6</span><span>3</span><span>4</span><span>5</span><span>6</span><span>7</span><span>8</span><span class="sun">9</span></div>
    <div class="week"><span class="kw">7</span><span>10</span><span>11</span><span>12</span><span>13</span><span>14</span><span>15</span><span class="sun">16</span></div>
    <div class="week"><span class="kw">8</span><span>17</span><span>18</span><span>19</span><span>20</span><span>21</span><span>22</span><span class="sun">23</span></div>
    <div class="week"><span class="kw">9</span><span>24</span><span>25</span><span>26</span><span>27</span><span>28</span><span></span><span></span></div>
  </div>

  <footer class="holidays">
    <div class="label">Feiertage<br>Holidays<br>Jours fériés</div>
    <dl class="holiday-list list-de">
      <dt>Neujahrstag</dt><dd>Jan 01</dd>
      <dt>Offenbarung (BW, BY &amp; ST)</dt><dd>Jan 06</dd>
      <dt>Weihnachtsfeiertag</dt><dd>Dez 25</dd>
      <dt>Weihnachtsfeiertage</dt><dd>Dez 26</dd>
    </dl>
    <dl class="holiday-list list-en">
      <dt>New Year's Day</dt><dd>01 January</dd>
      <dt>Epiphany</dt><dd>06 January</dd>
      <dt>Immaculate Conception</dt><dd>08 December</dd>
      <dt>Christmas Eve</dt><dd>24 December</dd>
      <dt>Christmas Day</dt><dd>25 December</dd>
      <dt>Boxing Day</dt><dd>26 December</dd>
      <dt>New Year</dt><dd>31 December</dd>
    </dl>
    <dl class="holiday-list list-fr">
      <dt>Jour de l'An</dt><dd>janv-01</dd>
      <dt>Noël</dt><dd>déc-25</dd>
      <dt>Saint-Étienne</dt><dd>déc-26</dd>
    </dl>
  </footer>

  <svg class="date-ring" viewBox="0 0 100 100" aria-label="Magnetischer Datumsring">
    <defs>
      <filter id="ring-shadow" x="-30%" y="-30%" width="160%" height="160%">
        <feDropShadow dx="0" dy="2" stdDeviation="2" flood-color="#000" flood-opacity=".35"/>
      </filter>
    </defs>
    <circle cx="50" cy="50" r="41" fill="none" stroke="var(--ring)" stroke-width="7" filter="url(#ring-shadow)"/>
  </svg>

</main>
</body>
</html>
```